Morvela Aesthetic Doctor

I require an elegant, luxurious looking business card for my aesthetic business. I am a doctor and that will set me aside from competitors. I am planning to provide home and spa based treatments to clients with high expectations. I have attached my logo.

```html
<!DOCTYPE html>
<html lang="en">
<head>
<meta charset="utf-8">
<title>Morvela Aesthetic Doctor – Business Card</title>
<link rel="stylesheet" href="https://fonts.googleapis.com/css2?family=Montserrat:wght@300;400;500;700&display=swap">
<style>
  :root {
    --bg: #e4e4e4;
    --card-white: #ffffff;
    --blue-deep: #1b7dc2;
    --blue-mid: #1ea7e1;
    --blue-dark: #1565b4;
    --blue-light: #56bde9;
    --blue-pale: #7fcdf0;
    --logo-grey: #9a9a9a;
    --text-white: #ffffff;
  }
  * { margin: 0; padding: 0; box-sizing: border-box; }
  html, body { width: 1200px; height: 900px; overflow: hidden; }
  body {
    background: var(--bg);
    font-family: "Montserrat", sans-serif;
    position: relative;
  }
  .card {
    position: absolute;
    left: 290px;
    width: 620px;
    height: 354px;
    overflow: hidden;
    box-shadow: 0 6px 18px rgba(0,0,0,0.12);
  }
  .card svg.waves { position: absolute; inset: 0; width: 100%; height: 100%; }
  .card-front { top: 66px; background: var(--card-white); }
  .card-back { top: 480px; background: var(--blue-deep); }

  .brand {
    position: absolute;
    left: 150px;
    top: 198px;
    display: flex;
    align-items: center;
    gap: 18px;
  }
  .brand-mark {
    width: 58px; height: 58px;
    border-radius: 50%;
    background: var(--blue-light);
  }
  .brand-name {
    font-family: "Montserrat", sans-serif;
    font-weight: 400;
    font-size: 30px;
    letter-spacing: 2px;
    color: var(--logo-grey);
    text-transform: uppercase;
    line-height: 1.1;
  }

  .contact {
    position: absolute;
    left: 48px;
    top: 58px;
    color: var(--text-white);
  }
  .contact-name {
    font-weight: 700;
    font-size: 34px;
    line-height: 1;
    text-transform: uppercase;
    letter-spacing: 0.5px;
  }
  .contact-title {
    margin-top: 12px;
    font-weight: 300;
    font-size: 20px;
  }
  .contact-diploma {
    margin-top: 4px;
    font-weight: 400;
    font-size: 13px;
  }
  .contact-list {
    list-style: none;
    margin-top: 20px;
    font-weight: 500;
    font-size: 21px;
  }
  .contact-list li {
    display: flex;
    align-items: center;
    gap: 10px;
    margin-bottom: 6px;
  }
  .contact-list svg { width: 20px; height: 20px; flex: none; }
</style>
</head>
<body>

<section class="card card-front" aria-label="Card front">
  <svg class="waves" viewBox="0 0 620 354" preserveAspectRatio="none" aria-hidden="true">
    <path d="M0 170 C120 110 230 110 330 100 C440 90 530 50 620 0 L0 0 Z" fill="var(--blue-light)"/>
    <path d="M0 185 C120 128 230 122 330 112 C450 98 540 62 620 18 L620 0 L0 0 Z" fill="var(--blue-mid)" opacity="0"/>
    <path d="M0 180 C130 120 240 112 340 102 C450 92 540 55 620 10 L620 0 L470 0 C400 40 330 60 250 72 C150 88 70 120 0 150 Z" fill="var(--blue-dark)"/>
    <path d="M0 150 C70 120 150 88 250 72 C330 60 400 40 470 0 L520 0 C440 50 350 72 260 86 C160 100 80 132 0 168 Z" fill="var(--blue-mid)"/>
    <path d="M0 175 C120 118 220 110 330 100 C450 88 540 52 620 8 L620 0 L0 0 Z" fill="none"/>
    <path d="M0 184 C130 126 240 118 345 108 C455 96 545 58 620 14 L620 0 C545 48 450 86 340 98 C230 108 120 120 0 172 Z" fill="var(--blue-mid)"/>
  </svg>
  <div class="brand">
    <span class="brand-mark" aria-hidden="true"></span>
    <span class="brand-name">Morvela Aesthetic Doctor</span>
  </div>
</section>

<section class="card card-back" aria-label="Card back">
  <svg class="waves" viewBox="0 0 620 354" preserveAspectRatio="none" aria-hidden="true">
    <path d="M470 0 C540 90 550 230 620 354 L620 0 Z" fill="var(--blue-mid)"/>
    <path d="M500 0 C560 100 570 240 620 330 L620 0 Z" fill="var(--blue-dark)"/>
    <path d="M540 0 C580 110 590 220 620 290 L620 0 Z" fill="var(--blue-light)"/>
    <path d="M575 0 C600 90 605 170 620 220 L620 0 Z" fill="var(--blue-pale)"/>
  </svg>
  <div class="contact">
    <h1 class="contact-name">Dr Lena<br>Varsk</h1>
    <p class="contact-title">MRCPCH MD</p>
    <p class="contact-diploma">Australasian Diploma of Aesthetic Medicine</p>
    <ul class="contact-list">
      <li>
        <svg viewBox="0 0 24 24" aria-hidden="true"><path fill="#fff" d="M6.6 10.8a15.1 15.1 0 0 0 6.6 6.6l2.2-2.2c.3-.3.7-.4 1-.2 1.1.4 2.3.6 3.6.6.6 0 1 .4 1 1V20c0 .6-.4 1-1 1A17 17 0 0 1 3 4c0-.6.4-1 1-1h3.5c.6 0 1 .4 1 1 0 1.3.2 2.5.6 3.6.1.3 0 .7-.2 1z"/></svg>
        0800 555 014
      </li>
      <li>
        <svg viewBox="0 0 24 24" aria-hidden="true"><rect x="2" y="5" width="20" height="14" rx="1" fill="#fff"/><path d="M2 6l10 7 10-7" fill="none" stroke="var(--blue-deep)" stroke-width="1.6"/></svg>
        lena@morvela.co.nz
      </li>
      <li>
        <svg viewBox="0 0 24 24" aria-hidden="true"><g fill="none" stroke="#fff" stroke-width="1.8"><circle cx="12" cy="12" r="9"/><ellipse cx="12" cy="12" rx="4" ry="9"/><path d="M3 12h18M5 7h14M5 17h14"/></g></svg>
        www.morvela.co.nz
      </li>
    </ul>
  </div>
</section>

</body>
</html>
```